Upgrade 4 Images - Bid 1, then we can discuss the other 3

We have a four graphics that we use in various presentations and business proposals. We want to upgrade them to make them really pop and match the level of service we provide, without going overboard.

We're open to new ideas, but the general form and content should stay the same.

I'd like to have all four designed by the same person, but I'm assuming this bid will be for 1 of the four, and then the other three can be contracted as additions.

```html
<!DOCTYPE html>
<html lang="en">
<head>
<meta charset="utf-8">
<title>Automation Reference Model</title>
<link rel="stylesheet" href="https://fonts.googleapis.com/css2?family=Righteous&family=Montserrat:wght@800&display=swap">
<style>
  :root {
    --sky: #bfe2f2;
    --sky-mid: #a8d9f2;
    --column: #96cdef;
    --column-deep: #8cc6eb;
    --navy: #203746;
    --navy-deep: #182b37;
    --gold: #f8b133;
    --gold-deep: #e99d1c;
    --white: #ffffff;
    --mist: #aab4bc;
    --screen-a: #f7fafc;
    --screen-b: #dde6ec;
  }
  * { margin: 0; padding: 0; box-sizing: border-box; }
  html, body { width: 1200px; height: 801px; overflow: hidden; background: var(--sky); }
  .model {
    position: relative;
    width: 1200px;
    height: 801px;
    background: var(--sky);
    font-family: "Righteous", sans-serif;
    overflow: hidden;
  }
  .backdrop, .connectors { position: absolute; inset: 0; }
  .title {
    position: absolute;
    left: 125px; top: 31px; width: 929px;
    text-align: center;
    white-space: nowrap;
    color: var(--gold);
    font-size: 46px;
    font-weight: 400;
    font-variant: small-caps;
    letter-spacing: 1px;
    line-height: 1;
  }
  .card {
    position: absolute;
    width: 155px;
    background: linear-gradient(180deg, var(--navy) 0%, var(--navy-deep) 100%);
    border-radius: 12px;
    box-shadow: 3px 5px 0 rgba(32,55,70,0.16), 0 10px 18px rgba(32,55,70,0.14);
  }
  .card-number {
    position: absolute;
    left: 50%; top: -22px;
    width: 44px; height: 44px;
    margin-left: -22px;
    border-radius: 50%;
    background: radial-gradient(circle at 35% 30%, #fcc45a, var(--gold) 55%, var(--gold-deep));
    box-shadow: 0 2px 4px rgba(24,43,55,0.3);
    color: var(--navy);
    font-family: "Montserrat", sans-serif;
    font-weight: 800;
    font-size: 30px;
    line-height: 44px;
    text-align: center;
  }
  .card-rule {
    position: absolute;
    left: 10px; right: 10px; top: 33px;
    height: 5px;
    background: radial-gradient(circle, var(--gold) 2px, transparent 2.4px) 0 0 / 7px 5px repeat-x;
  }
  .card-screen {
    position: absolute;
    background: linear-gradient(180deg, var(--screen-a), var(--screen-b));
    border: 2px solid var(--white);
    border-radius: 2px;
    box-shadow: 0 2px 5px rgba(0,0,0,0.25);
  }
  .badge {
    position: absolute;
    border-radius: 50%;
    background: var(--white);
    color: var(--navy);
  }
  .badge-in {
    left: 32px; top: 338px; width: 124px; height: 124px;
    box-shadow: 0 0 0 6px var(--sky-mid), 0 0 0 7px var(--gold);
  }
  .badge-with {
    left: 1029px; top: 331px; width: 138px; height: 138px;
    box-shadow: 0 0 0 7px var(--sky-mid), 0 0 0 8px var(--navy);
  }
  .badge-lines { position: absolute; font-size: 17px; line-height: 21px; }
  .badge-in .badge-lines { left: 23px; top: 18px; }
  .badge-with .badge-lines { left: 28px; top: 22px; }
  .brand { display: block; color: var(--mist); font-size: 22px; line-height: 28px; letter-spacing: 0.5px; }
  .pillar-label {
    position: absolute;
    top: 721px;
    width: 156px;
    text-align: center;
    white-space: nowrap;
    color: var(--gold);
    font-size: 19px;
    letter-spacing: 0.5px;
  }
</style>
</head>
<body>
<main class="model">
  <svg class="backdrop" width="1200" height="801" viewBox="0 0 1200 801" aria-hidden="true">
    <defs>
      <linearGradient id="pillar" x1="0" y1="0" x2="0" y2="1">
        <stop offset="0" stop-color="var(--column-deep)"/>
        <stop offset="1" stop-color="var(--column)"/>
      </linearGradient>
    </defs>
    <g fill="url(#pillar)">
      <polygon points="201,0 356,0 356,700 278,667 201,700"/>
      <polygon points="410,0 565,0 565,700 488,667 410,700"/>
      <polygon points="619,0 774,0 774,700 697,667 619,700"/>
      <polygon points="828,0 984,0 984,700 906,667 828,700"/>
    </g>
    <polygon fill="var(--sky-mid)" points="0,264 146,264 179,400 146,537 0,537"/>
    <polygon fill="var(--sky-mid)" points="1017,150 1157,264 1191,400 1157,537 1017,652"/>
    <path fill="var(--navy)" d="M125,25 H1054 V74 Q1054,90 1038,91 L590,122 L142,91 Q125,90 125,74 Z"/>
    <g fill="var(--navy)">
      <polygon points="201,719 278,686 356,719 356,801 201,801"/>
      <polygon points="410,719 488,686 565,719 565,801 410,801"/>
      <polygon points="619,719 697,686 774,719 774,801 619,801"/>
      <polygon points="828,719 906,686 984,719 984,801 828,801"/>
    </g>
    <path fill="none" stroke="var(--gold)" stroke-width="4" stroke-linecap="round" d="M987,151 Q1008,151 1008,175 V380 Q1008,400 1040,400 Q1008,400 1008,420 V626 Q1008,651 987,651"/>
  </svg>

  <svg class="connectors" width="1200" height="801" viewBox="0 0 1200 801" aria-hidden="true">
    <g fill="none" stroke="var(--gold)" stroke-width="3" stroke-linecap="round" stroke-dasharray="0 7">
      <path d="M165,400 H196"/>
      <path d="M359,400 H380 M380,313 V489 M380,313 H404 M380,489 H404"/>
      <path d="M568,313 H589 M568,489 H589 M589,313 V489 M589,313 H613 M589,489 H613"/>
      <path d="M777,313 H791 M777,489 H791 M791,313 V489 M791,400 H821"/>
      <path d="M805,232 V576 M805,232 H821 M805,576 H821"/>
    </g>
    <g fill="var(--gold)">
      <polygon points="405,302 418,313 405,324"/>
      <polygon points="405,478 418,489 405,500"/>
      <polygon points="614,302 627,313 614,324"/>
      <polygon points="614,478 627,489 614,500"/>
      <polygon points="823,221 836,232 823,243"/>
      <polygon points="823,389 836,400 823,411"/>
      <polygon points="823,565 836,576 823,587"/>
    </g>
  </svg>

  <h1 class="title">Automation Reference Model</h1>

  <div class="badge badge-in">
    <p class="badge-lines">Do<br>More<br>in<span class="brand">Lumora</span></p>
  </div>
  <div class="badge badge-with">
    <p class="badge-lines">Do<br>More<br>with<span class="brand">Lumora</span></p>
  </div>

  <section class="card" style="left:201px; top:321px; height:158px;">
    <span class="card-number">1</span><span class="card-rule"></span>
    <div class="card-screen" role="img" aria-label="Screen of automated workflow runs with status lanes" style="left:16px; top:50px; width:124px; height:90px;"></div>
  </section>
  <section class="card" style="left:410px; top:247px; height:129px;">
    <span class="card-number">2</span><span class="card-rule"></span>
    <div class="card-screen" role="img" aria-label="Screen of a workflow template library with toggles" style="left:13px; top:50px; width:128px; height:60px;"></div>
  </section>
  <section class="card" style="left:410px; top:424px; height:129px;">
    <span class="card-number">3</span><span class="card-rule"></span>
    <div class="card-screen" role="img" aria-label="Screen of workflow parameter settings" style="left:14px; top:50px; width:126px; height:60px;"></div>
  </section>
  <section class="card" style="left:619px; top:247px; height:138px;">
    <span class="card-number">4</span><span class="card-rule"></span>
    <div class="card-screen" role="img" aria-label="Screen listing custom operation steps" style="left:44px; top:44px; width:62px; height:85px;"></div>
  </section>
  <section class="card" style="left:619px; top:424px; height:129px;">
    <span class="card-number">5</span><span class="card-rule"></span>
    <div class="card-screen" role="img" aria-label="Screen of custom scripted settings table" style="left:14px; top:50px; width:127px; height:60px;"></div>
  </section>
  <section class="card" style="left:828px; top:158px; height:129px;">
    <span class="card-number">6</span><span class="card-rule"></span>
    <div class="card-screen" role="img" aria-label="Processing report table" style="left:15px; top:47px; width:126px; height:74px;"></div>
  </section>
  <section class="card" style="left:828px; top:336px; height:129px;">
    <span class="card-number">7</span><span class="card-rule"></span>
    <div class="card-screen" role="img" aria-label="Job statistics table with data bars" style="left:15px; top:47px; width:126px; height:70px;"></div>
  </section>
  <section class="card" style="left:828px; top:514px; height:129px;">
    <span class="card-number">8</span><span class="card-rule"></span>
    <div class="card-screen" role="img" aria-label="Dashboard with treemap and bar charts" style="left:13px; top:47px; width:130px; height:76px;"></div>
  </section>

  <p class="pillar-label" style="left:201px;">Automation</p>
  <p class="pillar-label" style="left:410px;">Flexibility</p>
  <p class="pillar-label" style="left:619px;">Customization</p>
  <p class="pillar-label" style="left:828px;">Insight</p>
</main>
</body>
</html>
```